Web Design Project

The client is unsure if they want a completely new design or a design that matches their existing site closely (https://www.kelvatcover.com.au). So essentially we are looking for some designs that reflect the existing sites shape and colour and some designs that have their own new style. The company will sell three main types of insurance, Car, Bike and Caravan.

Read the complete brief and in the attached document.
The logo is also attached

I have also attached a zip of a few classic cars, if you can incorporate those.

Industry/Entity Type

Insurance

Requirements
Should not have
• Print This Page
Site Search

```html
<!DOCTYPE html>
<html lang="en">
<head>
<meta charset="utf-8">
<title>Kelvat Cover – Insure with an Enthusiast</title>
<link href="https://fonts.googleapis.com/css2?family=Open+Sans:wght@400;600;700&family=Arimo:wght@400;700&family=Roboto+Condensed:wght@300;400&display=swap" rel="stylesheet">
<style>
:root{
  --black:#1b1b1b;
  --orange:#f06a1a;
  --orange-dark:#e8401f;
  --red:#e42a23;
  --accent:#f47a20;
  --body-bg:#ececec;
  --line:#d4d4d4;
  --text:#333;
  --white:#fff;
  --foot-text:#d8d8d8;
  --claim-blue:#1d8fd0;
}
*{box-sizing:border-box;margin:0;padding:0}
html,body{width:1200px;height:1167px;overflow:hidden}
body{position:relative;background:var(--body-bg);font-family:"Arimo",Arial,sans-serif;color:var(--text)}
.abs{position:absolute}
.hl{color:var(--accent)}

.top-strip{left:0;top:0;width:1200px;height:30px;background:var(--black)}
.header{left:0;top:30px;width:1200px;height:110px;background:linear-gradient(180deg,var(--orange) 0%,var(--orange-dark) 100%)}
.brand{display:flex;align-items:center;justify-content:center;gap:8px;width:167px;height:56px;border-radius:50%;background:var(--black);color:var(--white);font-family:"Open Sans",sans-serif;font-size:16px;font-weight:400;letter-spacing:.5px;white-space:nowrap}
.brand-dot{width:9px;height:9px;border-radius:50%;background:var(--white)}
.header .brand{left:218px;top:25px}
.tagline{left:396px;top:60px;font-family:"Open Sans",sans-serif;font-size:20px;color:var(--white);white-space:nowrap}
.broker{left:920px;top:34px;font-family:"Open Sans",sans-serif;font-weight:700;font-size:10.5px;color:var(--white)}
.phone-ico{left:748px;top:58px;width:28px;height:28px;background:var(--white);display:flex;align-items:center;justify-content:center}
.call{left:790px;top:62px;font-family:"Open Sans",sans-serif;font-size:18px;color:var(--white);white-space:nowrap}

.nav{left:3px;top:140px;width:1197px;height:39px;background:linear-gradient(180deg,#3a3a3a,#141414)}
.nav ul{list-style:none;position:absolute;left:0;top:0;height:39px}
.nav li{position:absolute;top:0;height:39px;line-height:39px;font-family:"Open Sans",sans-serif;font-weight:600;font-size:10.5px;color:#e6e6e6;text-align:center;border-right:1px solid #444;white-space:nowrap}

.hero-band{left:0;top:179px;width:1200px;height:334px;background:var(--red)}
.hero{left:196px;top:190px;width:800px;height:305px;background:var(--white);box-shadow:0 8px 10px -6px rgba(0,0,0,.45)}
.hero-photo{left:0;top:0;width:552px;height:305px;background:linear-gradient(180deg,#cfcfcf 0%,#8a8a8a 45%,#9a1d1d 62%,#6b6b6b 85%,#3a3a3a 100%)}
.hero-caption{left:0;top:256px;width:552px;height:49px;background:rgba(20,20,20,.82);font-family:"Open Sans",sans-serif;font-size:19px;color:var(--white);line-height:49px;padding-left:13px;white-space:nowrap}
.register{left:581px;top:15px;width:193px;height:44px;border-radius:5px;background:linear-gradient(180deg,#f9892c,#ef5f12);display:flex;align-items:center;gap:5px;padding-left:10px;color:var(--white);font-family:"Open Sans",sans-serif;font-weight:700;font-size:22px;letter-spacing:-.3px;white-space:nowrap;overflow:hidden}
.product{width:207px;height:61px;background:linear-gradient(180deg,#fafafa,#ececec);border:1px solid #ddd}
.product span{position:absolute;left:8px;top:19px;font-family:"Open Sans",sans-serif;font-size:15px;color:#222;white-space:nowrap}
.product .art{position:absolute;right:4px;top:4px;width:80px;height:52px;border-radius:6px}
.quote{left:606px;top:229px;display:flex;align-items:center;gap:4px}
.quote-box{font-family:"Arimo",sans-serif;color:#111;font-size:10px;line-height:12px}
.quote-box b{display:block;background:#111;color:var(--white);font-size:14px;padding:2px 6px;border-radius:3px}

.intro-title{left:211px;top:540px;font-family:"Open Sans",sans-serif;font-weight:400;font-size:18px;color:#333;white-space:nowrap}
.intro{left:209px;top:573px;width:514px;font-size:10.5px;line-height:15px;text-align:justify;text-align-last:justify;color:#333}
.detail{left:653px;top:640px;font-size:10.5px;color:#333}

.claim{left:748px;top:545px;width:249px;height:99px;background:linear-gradient(180deg,#fff,#ececec);border:1px solid #ddd}
.claim-title{left:14px;top:10px;font-family:"Open Sans",sans-serif;font-size:16px;color:#222}
.claim-figure{left:900px;top:513px;width:50px;height:82px;border-radius:20px 20px 4px 4px;background:linear-gradient(180deg,#d8b878,#3a302a)}
.claim-btn{left:882px;top:592px;width:70px;height:51px;border-radius:6px;background:linear-gradient(180deg,#4fb5ea,var(--claim-blue));border:2px solid #eaf6ff;color:var(--white);font-family:"Open Sans",sans-serif;font-weight:700;font-size:16px;line-height:18px;text-align:center;padding-top:6px}

.card{background:linear-gradient(180deg,#fbfbfb,#efefef);border:1px solid var(--line)}
.card-icon{position:absolute;left:10px;top:10px;width:36px;height:32px;border-radius:4px;background:linear-gradient(180deg,#eee,#aaa)}
.card-title{position:absolute;left:62px;top:18px;font-family:"Open Sans",sans-serif;font-size:14px;color:#222;white-space:nowrap}
.item{position:absolute;font-size:10px;line-height:18.5px;color:#222}
.item b{display:block;font-size:10.5px}
.item b::before{content:"";display:inline-block;border-left:4px solid #222;border-top:3px solid transparent;border-bottom:3px solid transparent;margin-right:5px;vertical-align:1px}
.more{position:absolute;font-size:10.5px;color:#333;white-space:nowrap}

.policy-title{left:18px;top:14px;font-family:"Open Sans",sans-serif;font-size:16px;color:#333;white-space:nowrap}
.benefits{position:absolute;left:22px;top:44px;list-style:none;font-size:10px;line-height:15px;color:#222}
.benefits li{padding-left:15px;position:relative;white-space:nowrap}
.benefits li::before{content:"›";position:absolute;left:0;top:-1px;font-size:13px}

.affil{left:204px;top:867px;width:792px;height:80px;background:linear-gradient(180deg,#fafafa,#eee);border:1px solid var(--line)}
.affil h3{position:absolute;left:30px;top:10px;font-family:"Open Sans",sans-serif;font-weight:600;font-size:14px;color:#111}
.badge{position:absolute;top:34px;height:32px;border-radius:3px}

.footer{left:0;top:961px;width:1200px;height:181px;background:var(--black)}
.foot-bottom{left:0;top:1142px;width:1200px;height:25px;background:#262626;text-align:center;line-height:25px;font-size:10.5px;color:#8a8a8a}
.foot-bottom span{font-size:12px;color:#a5a5a5}
.f-head{font-family:"Open Sans",sans-serif;font-weight:600;color:var(--white);white-space:nowrap}
.qlinks{position:absolute;list-style:none;font-family:"Roboto Condensed",sans-serif;font-weight:300;font-size:11.5px;line-height:16.7px;color:var(--foot-text);text-transform:uppercase}
.qlinks li{padding-left:15px;position:relative;white-space:nowrap}
.qlinks li::before{content:"";position:absolute;left:0;top:4px;border-left:6px solid var(--white);border-top:4px solid transparent;border-bottom:4px solid transparent}
.contact{left:575px;font-size:12.2px;line-height:16.7px;color:var(--foot-text);white-space:nowrap}
.social{width:20px;height:20px;border-radius:4px}
.newsletter{left:807px;width:196px;height:20px;border-radius:10px;background:linear-gradient(180deg,#8c8c8c,#6e6e6e);font-family:"Open Sans",sans-serif;font-style:italic;font-size:11px;line-height:20px;padding-left:13px;color:#eee}
.footer-brand{left:848px;width:139px;height:47px;font-size:13px;background:#333;border:1px solid #777}
</style>
</head>
<body>

<div class="abs top-strip"></div>

<header class="abs header">
  <div class="abs brand"><span class="brand-dot"></span>Kelvat Cover</div>
  <div class="abs tagline">Insure with an Enthusiast</div>
  <div class="abs broker">BROKER LOGIN</div>
  <div class="abs phone-ico">
    <svg width="20" height="20" viewBox="0 0 24 24"><circle cx="12" cy="12" r="11" fill="#111"/><path d="M8.5 6.5c.6-.4 1.2-.3 1.5.2l1.2 2c.3.5.2 1-.2 1.3l-.8.6c.5 1.4 1.5 2.6 2.9 3.3l.7-.7c.4-.4.9-.4 1.3-.1l1.9 1.3c.5.3.6 1 .2 1.5-.8 1-2 1.5-3.2 1-3.3-1.3-5.7-4-6.5-7.4-.3-1.2.2-2.3 1-3z" fill="#fff"/></svg>
  </div>
  <div class="abs call">CALL NOW &nbsp;: 1300 555 014</div>
</header>

<nav class="abs nav">
  <ul>
    <li style="left:189px;width:84px">HOME</li>
    <li style="left:273px;width:99px">ABOUT US</li>
    <li style="left:372px;width:99px">INSURANCE</li>
    <li style="left:471px;width:98px">EVENTS</li>
    <li style="left:569px;width:98px">CLUBS</li>
    <li style="left:667px;width:98px">LINKS</li>
    <li style="left:765px;width:100px">FAQ</li>
    <li style="left:865px;width:98px">CONTACT US</li>
  </ul>
</nav>

<div class="abs hero-band"></div>
<section class="abs hero">
  <div class="abs hero-photo" role="img" aria-label="Photograph of a red classic convertible parked on a grey tree-lined lawn"></div>
  <div class="abs hero-caption">Specialised <span class="hl">Insurance</span> for Classic and Prestige <span class="hl">Cars</span> and <span class="hl">Bikes</span></div>
  <div class="abs register">
    <svg width="24" height="30" viewBox="0 0 30 34"><path d="M4 2l20 15L4 32l-2-4 15-11L2 6z" fill="#fff"/></svg>
    register now
  </div>
  <div class="abs product" style="left:574px;top:78px">
    <span>Car <span class="hl" style="position:static">Insurance</span></span>
    <div class="art" role="img" aria-label="Illustration of a red sports car" style="background:linear-gradient(180deg,#f3f3f3,#d92a2a 55%,#9a1515)"></div>
  </div>
  <div class="abs product" style="left:574px;top:152px">
    <span>Bike <span class="hl" style="position:static">Insurance</span></span>
    <div class="art" role="img" aria-label="Illustration of an orange and blue sport motorbike" style="width:60px;background:linear-gradient(135deg,#ee5a1e,#2d6fd0)"></div>
  </div>
  <div class="abs quote">
    <svg width="34" height="32" viewBox="0 0 34 32"><rect x="1" y="8" width="22" height="22" fill="#f4e9a6" stroke="#888"/><path d="M5 17l6 7L31 2" fill="none" stroke="#d41a1a" stroke-width="4"/></svg>
    <div class="quote-box">&nbsp;REQUEST A<b>FREE Quote</b></div>
  </div>
</section>

<h2 class="abs intro-title">At Kelvat, we love your ride, just as much as you do.</h2>
<p class="abs intro"><b>Kelvat Cover was established to offer some competition in the marketplace for insuring Classic and Prestige Vehicle owners pride and joy.</b>&nbsp; Kelvat Cover is a boutique insurance company that specifically caters to classic and prestige vehicle owners, whether they be cars or bikes.&nbsp; Founded by Dale Kessing in 2006, hence where the name comes from, Kelvat Cover prides itself on its customer.</p>
<div class="abs detail">GET DETAIL +</div>

<section class="abs claim">
  <div class="abs claim-title">Make a <span class="hl">Claim</span></div>
</section>
<div class="abs claim-figure" role="img" aria-label="Illustration of a claims officer holding a clipboard"></div>
<div class="abs claim-btn">Claim<br>Now</div>

<section class="abs card" style="left:204px;top:668px;width:257px;height:183px">
  <div class="card-icon" role="img" aria-label="Newspaper icon"></div>
  <div class="card-title"><span class="hl">Latest</span> News</div>
  <div class="item" style="left:8px;top:51px;width:246px"><b>New products launced</b><span style="padding-left:8px;display:block">Our team of trained professionals with over 80 years experience</span></div>
  <div class="item" style="left:6px;top:109px;width:246px"><b>New products launced</b><span style="padding-left:8px;display:block">Our team of trained professionals with over 80 years experience</span></div>
  <div class="more" style="left:142px;top:162px">SHOW ALL NEWS +</div>
</section>

<section class="abs card" style="left:475px;top:668px;width:249px;height:183px">
  <div class="card-icon" role="img" aria-label="Calendar icon"></div>
  <div class="card-title" style="left:49px"><span class="hl">Upcoming</span> Events</div>
  <div class="item" style="left:10px;top:53px;width:238px"><b>New products launced</b><span style="display:block">Our team of trained professionals with over 80 years experience</span></div>
  <div class="item" style="left:10px;top:109px;width:238px"><b>New products launced</b><span style="display:block;padding-left:2px">Our team of trained professionals with over 80 years experience</span></div>
  <div class="more" style="left:126px;top:162px">SHOW ALL EVENTS +</div>
</section>

<section class="abs card" style="left:747px;top:654px;width:249px;height:198px">
  <div class="abs policy-title">OUR POLICY <span class="hl">BENEFITS</span></div>
  <ul class="benefits">
    <li>Agreed Value</li>
    <li>New Replacement Vehicle in first 2 years</li>
    <li>Choice of Repairer</li>
    <li>Lifetime Guarantee for Repairs</li>
    <li>Free Windscreen/Glass Benefit</li>
    <li>Hire car following accident or theft</li>
    <li>Flexible coverage</li>
    <li>Pay Premiums by Instalments</li>
    <li>Salvage retained by you on<br>vehicles over 30 years</li>
  </ul>
</section>

<section class="abs affil">
  <h3>AFFILIATIONS</h3>
  <div class="badge" style="left:36px;width:104px;background:#e6c31a"></div>
  <div class="badge" style="left:152px;width:108px;background:#cfd6de"></div>
  <div class="badge" style="left:270px;top:50px;height:16px;width:100px;background:#3a3a3a"></div>
  <div class="badge" style="left:382px;top:21px;height:40px;width:70px;background:#d42a2a"></div>
  <div class="badge" style="left:464px;width:100px;background:#b8231e"></div>
  <div class="badge" style="left:577px;top:28px;width:56px;background:#e2473a"></div>
</section>

<footer class="abs footer">
  <div class="abs f-head" style="left:223px;top:8px;font-size:16px">Quick Links</div>
  <ul class="qlinks" style="left:212px;top:45px">
    <li>About us</li><li>Terms and conditions</li><li>Car insurance</li><li>Bike insurance</li><li>Career</li>
  </ul>
  <ul class="qlinks" style="left:392px;top:47px">
    <li>Events</li><li>Clubs</li><li>Register</li><li>Links</li><li>Contact us</li>
  </ul>
  <div class="abs f-head" style="left:575px;top:13px;font-size:13px">Contact Information</div>
  <div class="abs contact" style="top:39px">
    Kelvat Cover Services<br>42 Marlow Street<br>Harwood Vale Qld 4110<br><br>Ph: 1300 555 014<br>Fx: 1300 555 029<br>admin@kelvatcover.com.au
  </div>
  <div class="abs f-head" style="left:766px;top:14px;font-size:13px">Socialize with us:</div>
  <div class="abs social" style="left:891px;top:10px;background:#f07a1a"></div>
  <div class="abs social" style="left:922px;top:10px;background:#3fa7e0"></div>
  <div class="abs social" style="left:952px;top:10px;background:#3b5f9e"></div>
  <div class="abs social" style="left:982px;top:10px;background:#2a7ab8"></div>
  <div class="abs f-head" style="left:816px;top:51px;font-size:12px">Subscribe to our Newsletter</div>
  <div class="abs newsletter" style="top:77px">Your E-Mail Address</div>
  <div class="abs brand footer-brand" style="top:114px"><span class="brand-dot"></span>Kelvat Cover</div>
</footer>

<div class="abs foot-bottom">Copyright © <span>Kelvat Cover Services</span> &nbsp; 2013 &nbsp;All Rights Reserved</div>

</body>
</html>
```